a board game needs a good card design (5 cards in the same design)

We need a redesign for our cards.
Each card file is 63*88mm, 3mm bleeds - 69mm*94mm, should be done vector and CMYK, because it will be printed.

The game includes 108 cards (don't worry, no needs to design them all), it has:
numbers from 1 to 20 on the yellow background
from 6 to 20 on the green background
+1, +2, +3, +4, +5 on the white background with our logo,
special card on blue background (now it's "+", but it's not necessary, it could be anything with positive meaning, because it's kind of joker card)
circle on red background. We don't want see this circle anymore, it should be replaced to something else. It's the worst card, so the player who draws should understand "oops, that's not good!".

What we need:
now cards look boring and simple, it should look funnier, people hold them and know it's a fun game.
We expect in return 5 cards:
1) any number on the green background
2) any number on the yellow bg.
3) +5 on the white bg with our logo. The white card means the next person should Pick Pile, so we're fine with our logo on the background, but if you can make up something more interesting, would be great.
4) something on the red bg, what means danger, for a card which could be hard to get rid of
5) something positive on the blue bg, what means you have 2 turns instead of 1, can play this card on any card and place any card on top of it (could sound complicated, just know it's a good card to have)

I've written "color of the background", but these colors are not necessary to come from the background, just overall color of the card should have these primary colors.

All cards should have a big number or whatever in the center and small copies in 2 corners as on standard cards.

Would be great to not make your own font for digits, because we should be able to copy the design to all numbers used.

I have uploaded our logo and current basic design of our cards.

Target Market(s)

the game is suitable for meetup with friends or family play. So it could be anyone from 7 years old to 99

Font styles to use
Sans Serif

Colors
0792cd
ec1f27
fbed22
ffffff
9bcb3b

Requirements
Must have
• the cards must have a number or symbol in the center and on 2 corners (upside down on the bottom corner). Each card must have primary color.
Nice to have
• something on the background, not just color-background. Please use the logo for the background for the white card only.
Should not have
• words, animals, flowers etc
• symbols and digits only please.

```html
<!DOCTYPE html>
<html lang="en">
<head>
<meta charset="utf-8">
<title>Pick Pile – Card Set</title>
<link rel="stylesheet" href="https://fonts.googleapis.com/css2?family=Arimo:wght@700&family=Varela+Round&display=swap">
<style>
  :root{
    --blue:#0792cd; --blue-dark:#0a6a99;
    --red:#e2302b; --red-dark:#b11c22;
    --yellow:#f4e922; --yellow-dark:#d2c61c;
    --green:#9bcb3b; --green-dark:#6f9a2a;
    --white:#ffffff; --paper:#f1f1f1; --grey:#6d6d6d; --ink:#111111;
  }
  html,body{margin:0;padding:0;}
  body{width:1200px;height:1200px;overflow:hidden;background:var(--white);position:relative;}
  .card{position:absolute;width:320px;height:453px;display:block;overflow:hidden;}
  .card--back{left:56px;top:102px;width:308px;height:440px;}
  .card--red{left:438px;top:104px;}
  .card--green{left:828px;top:102px;}
  .card--white{left:53px;top:642px;}
  .card--blue{left:442px;top:640px;}
  .card--yellow{left:840px;top:640px;}

  .fill-blue{fill:var(--blue);} .fill-blue-dark{fill:var(--blue-dark);}
  .fill-red{fill:var(--red);} .fill-red-dark{fill:var(--red-dark);}
  .fill-yellow{fill:var(--yellow);} .fill-yellow-dark{fill:var(--yellow-dark);}
  .fill-green{fill:var(--green);} .fill-green-dark{fill:var(--green-dark);}
  .fill-white{fill:var(--white);} .fill-paper{fill:var(--paper);}

  .digit{font-family:"Varela Round",sans-serif;fill:var(--white);}
  .digit--big{font-size:300px;}
  .digit--corner{font-size:44px;}
  .plus{font-family:"Arimo",sans-serif;font-weight:700;fill:var(--grey);}
  .plus--big{font-size:200px;}
  .plus--corner{font-size:40px;}
  .brand{font-family:"Arimo",sans-serif;font-weight:700;}
  .brand--back{font-size:46px;fill:var(--blue);}
  .brand--small{font-size:26px;fill:var(--blue);}
  .brand--circle{font-size:50px;fill:var(--white);}
  .ring{fill:none;stroke:var(--grey);stroke-width:20;}
  .edge{fill:none;stroke:var(--ink);stroke-width:3;}
</style>
</head>
<body>

<!-- Card back -->
<svg class="card card--back" viewBox="0 0 385 550" aria-label="Card back">
  <defs>
    <linearGradient id="back-tone" x1="0" y1="0" x2="1" y2="1">
      <stop offset="0" stop-color="#f6ea2a"/>
      <stop offset="0.5" stop-color="#f7ee6e"/>
      <stop offset="1" stop-color="#f6ea2a"/>
    </linearGradient>
  </defs>
  <rect width="385" height="550" rx="22" fill="url(#back-tone)" role="img" aria-label="Yellow diamond checker pattern"/>
  <rect x="44" y="200" width="297" height="150" rx="16" class="fill-white"/>
  <text class="brand brand--back" x="192" y="290" text-anchor="middle">PICK PILE</text>
</svg>

<!-- Red danger card -->
<svg class="card card--red" viewBox="0 0 400 566">
  <defs><clipPath id="shape-red"><rect width="400" height="566" rx="28"/></clipPath></defs>
  <g clip-path="url(#shape-red)">
    <rect width="400" height="566" class="fill-red"/>
    <rect x="16" y="20" width="368" height="528" rx="14" class="fill-red-dark"/>
    <rect x="24" y="27" width="352" height="513" rx="10" class="fill-white"/>
    <circle cx="46" cy="46" r="50" class="fill-red-dark"/>
    <circle cx="40" cy="40" r="50" class="fill-red"/>
    <circle cx="354" cy="522" r="50" class="fill-red-dark"/>
    <circle cx="360" cy="528" r="50" class="fill-red"/>
  </g>
  <circle cx="200" cy="270" r="162" class="fill-red"/>
  <path class="fill-white" d="M176 168 Q176 146 200 146 Q224 146 224 168 L214 300 Q212 312 200 312 Q188 312 186 300 Z"/>
  <circle cx="200" cy="356" r="25" class="fill-white"/>
</svg>

<!-- Green number card -->
<svg class="card card--green" viewBox="0 0 400 566">
  <defs><clipPath id="shape-green"><rect width="400" height="566" rx="28"/></clipPath></defs>
  <g clip-path="url(#shape-green)">
    <rect width="400" height="566" class="fill-green"/>
    <rect x="16" y="20" width="368" height="528" rx="14" class="fill-green-dark"/>
    <rect x="24" y="27" width="352" height="513" rx="10" class="fill-white"/>
    <circle cx="46" cy="46" r="50" class="fill-green-dark"/>
    <circle cx="40" cy="40" r="50" class="fill-green"/>
    <circle cx="354" cy="522" r="50" class="fill-green-dark"/>
    <circle cx="360" cy="528" r="50" class="fill-green"/>
  </g>
  <text class="digit digit--corner" x="40" y="58" text-anchor="middle">7</text>
  <text class="digit digit--corner" x="360" y="510" text-anchor="middle" transform="rotate(180 360 510)">7</text>
  <circle cx="200" cy="272" r="162" class="fill-green"/>
  <text class="digit digit--big" x="200" y="380" text-anchor="middle">7</text>
</svg>

<!-- White +5 card -->
<svg class="card card--white" viewBox="0 0 400 566">
  <defs><clipPath id="shape-white"><rect x="2" y="2" width="396" height="562" rx="28"/></clipPath></defs>
  <g clip-path="url(#shape-white)">
    <rect width="400" height="566" class="fill-white"/>
    <rect x="16" y="20" width="368" height="526" rx="12" class="fill-paper"/>
    <circle cx="40" cy="44" r="50" class="fill-paper"/>
    <circle cx="34" cy="38" r="50" class="fill-white"/>
    <circle cx="360" cy="522" r="50" class="fill-paper"/>
    <circle cx="366" cy="528" r="50" class="fill-white"/>
  </g>
  <rect x="2" y="2" width="396" height="562" rx="28" class="edge"/>
  <text class="plus plus--corner" x="36" y="54" text-anchor="middle">+5</text>
  <text class="plus plus--corner" x="364" y="512" text-anchor="middle" transform="rotate(180 364 512)">+5</text>
  <text class="brand brand--small" x="300" y="85" text-anchor="middle">PICK PILE</text>
  <text class="brand brand--small" x="100" y="490" text-anchor="middle" transform="rotate(180 100 482)">PICK PILE</text>
  <circle cx="199" cy="271" r="150" class="ring"/>
  <text class="plus plus--big" x="199" y="342" text-anchor="middle">+5</text>
</svg>

<!-- Blue joker card -->
<svg class="card card--blue" viewBox="0 0 400 566">
  <defs><clipPath id="shape-blue"><rect width="400" height="566" rx="28"/></clipPath></defs>
  <g clip-path="url(#shape-blue)">
    <rect width="400" height="566" class="fill-blue"/>
    <rect x="16" y="20" width="368" height="528" rx="14" class="fill-blue-dark"/>
    <rect x="24" y="27" width="352" height="513" rx="10" class="fill-white"/>
    <circle cx="46" cy="46" r="50" class="fill-blue-dark"/>
    <circle cx="40" cy="40" r="50" class="fill-blue"/>
    <circle cx="354" cy="522" r="50" class="fill-blue-dark"/>
    <circle cx="360" cy="528" r="50" class="fill-blue"/>
  </g>
  <circle cx="198" cy="272" r="162" class="fill-blue"/>
  <text class="brand brand--circle" x="198" y="290" text-anchor="middle">PICK PILE</text>
</svg>

<!-- Yellow number card -->
<svg class="card card--yellow" viewBox="0 0 400 566">
  <defs><clipPath id="shape-yellow"><rect width="400" height="566" rx="28"/></clipPath></defs>
  <g clip-path="url(#shape-yellow)">
    <rect width="400" height="566" class="fill-yellow"/>
    <rect x="16" y="20" width="368" height="528" rx="14" class="fill-yellow-dark"/>
    <rect x="24" y="27" width="352" height="513" rx="10" class="fill-white"/>
    <circle cx="46" cy="46" r="50" class="fill-yellow-dark"/>
    <circle cx="40" cy="40" r="50" class="fill-yellow"/>
    <circle cx="354" cy="522" r="50" class="fill-yellow-dark"/>
    <circle cx="360" cy="528" r="50" class="fill-yellow"/>
  </g>
  <text class="digit digit--corner" x="40" y="58" text-anchor="middle">7</text>
  <text class="digit digit--corner" x="360" y="510" text-anchor="middle" transform="rotate(180 360 510)">7</text>
  <circle cx="198" cy="272" r="162" class="fill-yellow"/>
  <text class="digit digit--big" x="198" y="380" text-anchor="middle">7</text>
</svg>

</body>
</html>
```